Advert for Services that we offer

Bolt Remova Ltd need an design to represent what we do in a modern way by showing an image with a brief description and the use of corporate logo the information we will proved vie a doc file and this is to be presented in a modern way. This design will be for print & web. we have done our own design and its not great i have put this in the file repository

Target Market(s)

Motor trade

Font styles to use
Sans Serif

Colors

Designer to choose colors to be used in the design.

Requirements
Must have
• Company colour scheme as per logo within the files uploaded.
• and a small boarder to isolate it from the rest of the articles.
Nice to have
• Modern font
Should not have
• Old style font

```html
<!DOCTYPE html>
<html lang="en">
<head>
<meta charset="utf-8">
<title>Bolt Remova Ltd – Product Testing &amp; Analysis</title>
<link rel="stylesheet" href="https://fonts.googleapis.com/css2?family=Montserrat:wght@300;400;600;700;800&display=swap">
<style>
  :root {
    --page-bg: #e6e8ea;
    --card-white: #ffffff;
    --brand-blue: #1565b8;
    --brand-blue-deep: #0e4f96;
    --brand-navy: #0c2748;
    --brand-sky: #a8d3f7;
    --photo-dark: #4a5a6c;
    --photo-light: #a9b4c0;
    --bar-grey: #d9d9d9;
    --ink: #1b1b1b;
  }
  html, body {
    margin: 0;
    padding: 0;
    width: 1200px;
    height: 966px;
    overflow: hidden;
    background: var(--page-bg);
    font-family: "Montserrat", sans-serif;
  }
  .advert {
    position: absolute;
    left: 20px;
    top: 74px;
    width: 1160px;
    height: 817px;
    box-shadow: 0 4px 14px rgba(0,0,0,0.18);
  }
  .advert svg { display: block; }
  .title { font-weight: 800; font-size: 54px; letter-spacing: 0.5px; }
  .title--navy { fill: var(--brand-navy); }
  .title--sky { fill: var(--brand-sky); }
  .title--white { fill: var(--card-white); }
  .title-amp { font-weight: 300; }
  .service { font-size: 28px; fill: var(--card-white); letter-spacing: 1px; }
  .service-strong { font-weight: 700; }
  .service-light { font-weight: 400; }
  .service-mark { fill: var(--brand-sky); opacity: 0.8; }
  .contact-text { font-size: 22px; fill: var(--ink); }
  .contact-text--phone { font-weight: 700; }
  .contact-text--web { font-weight: 400; font-size: 20px; }
  .company-name { font-weight: 700; font-size: 30px; fill: var(--brand-blue); letter-spacing: 1px; }
</style>
</head>
<body>
<div class="advert">
  <svg viewBox="0 0 1221 860" width="1160" height="817" xmlns="http://www.w3.org/2000/svg">
    <defs>
      <linearGradient id="photoTone" x1="0" y1="0" x2="1" y2="1">
        <stop offset="0" stop-color="var(--photo-light)"/>
        <stop offset="1" stop-color="var(--photo-dark)"/>
      </linearGradient>
    </defs>

    <!-- card -->
    <rect class="card" x="0" y="0" width="1221" height="860" fill="var(--card-white)"/>

    <!-- photograph area -->
    <g class="photo" role="img" aria-label="Technician in overalls measuring the bore of a large flanged metal part with a digital gauge in a workshop">
      <rect x="20" y="18" width="740" height="722" fill="url(#photoTone)"/>
      <polygon points="352,18 760,18 760,740 90,740 20,700 20,600" fill="#2a5d96" opacity="0.55"/>
    </g>

    <!-- main blue panel -->
    <polygon class="panel" points="744,8 1209,8 1209,668 854,668 792,768 402,768" fill="var(--brand-blue)"/>
    <polygon class="panel-band" points="635,251 1209,251 1209,551 500,551" fill="var(--brand-blue-deep)"/>

    <!-- heading -->
    <text class="title title--navy" x="1158" y="103" text-anchor="end">PRODUCT</text>
    <text class="title title--sky" x="1158" y="153" text-anchor="end">TESTING</text>
    <text class="title title--white" x="1158" y="203" text-anchor="end"><tspan class="title-amp">&amp; </tspan>ANALYSIS</text>
    <line x1="738" y1="230" x2="1158" y2="230" stroke="var(--brand-sky)" stroke-width="1" opacity="0.7"/>

    <!-- services -->
    <g class="services">
      <text class="service" x="1135" y="296" text-anchor="end"><tspan class="service-strong">METALLURGICAL</tspan><tspan class="service-light"> TESTING</tspan></text>
      <rect class="service-mark" x="1150" y="279" width="15" height="15"/>
      <text class="service" x="1135" y="352" text-anchor="end"><tspan class="service-strong">BEARING PRE-LOAD</tspan><tspan class="service-light"> TESTING</tspan></text>
      <rect class="service-mark" x="1150" y="335" width="15" height="15"/>
      <text class="service" x="1135" y="409" text-anchor="end"><tspan class="service-strong">BORE</tspan><tspan class="service-light"> MEASUREMENT</tspan></text>
      <rect class="service-mark" x="1150" y="392" width="15" height="15"/>
      <text class="service" x="1135" y="465" text-anchor="end"><tspan class="service-strong">NEW PRODUCT</tspan><tspan class="service-light"> EVALUATION</tspan></text>
      <rect class="service-mark" x="1150" y="448" width="15" height="15"/>
      <text class="service" x="1135" y="521" text-anchor="end"><tspan class="service-strong">PRODUCT ANALYSIS</tspan><tspan class="service-light"> &amp; REPORT</tspan></text>
      <rect class="service-mark" x="1150" y="504" width="15" height="15"/>
    </g>

    <!-- contact bar -->
    <g class="contact">
      <rect x="19" y="804" width="34" height="35" fill="var(--brand-blue)"/>
      <path d="M29 813 c1-1 3-1 4 0 l2 3 c1 1 0 2 -1 3 l-1 1 c1 3 3 5 6 6 l1-1 c1-1 2-2 3-1 l3 2 c1 1 1 3 0 4 l-2 1 c-7 0 -16 -9 -16 -16 z" fill="var(--card-white)"/>
      <rect x="59" y="804" width="229" height="35" fill="var(--bar-grey)"/>
      <text class="contact-text contact-text--phone" x="67" y="830">0161 555 0192</text>

      <rect x="294" y="804" width="35" height="35" fill="var(--brand-blue)"/>
      <g fill="none" stroke="var(--card-white)" stroke-width="1.6">
        <circle cx="311.5" cy="821.5" r="9"/>
        <ellipse cx="311.5" cy="821.5" rx="4" ry="9"/>
        <line x1="302.5" y1="821.5" x2="320.5" y2="821.5"/>
      </g>
      <polygon points="335,804 790,804 777,839 335,839" fill="var(--bar-grey)"/>
      <text class="contact-text contact-text--web" x="347" y="830">WWW.BOLT-REMOVA.CO.UK</text>
    </g>

    <!-- company name -->
    <text class="company-name" x="1024" y="808" text-anchor="middle">BOLT REMOVA LTD</text>
  </svg>
</div>
</body>
</html>
```